依頼詳細
同一監修者の最近の書籍の表紙写真を添付しますので参考にしてください。できるだけイメージのやさしい感じで、かわいいデザインがいいです。
記載項目
表紙に記載して欲しいものすべて、添付のPDFに記入してあります。
希望イメージ
シンプル 複雑
単色 カラフル
暗い 明るい
日常 高級
遊び心 厳粛
未来的 伝統的
女性的 男性的
希望する色
納品ファイル
• 高解像度JPG (.jpg)
• イラストレーター形式 (.ai)
補足説明
当社は出版社ですから、時々、このような書籍の表紙デザインをクリエモアでお願いしています。
重要事項(書籍のサイズ等)を記入し忘れるという発注者側の重大なミスがあり、デザイナーさんたちに大変迷惑をかけましたので、消失時間を補うために募集期間を変更しました。よろしくお願いいたします。

この書籍の趣旨をシンプルですが、とても分かりやすくデザイン表示していただきました。good job でした。

修正案件を含めて『33件』ものご提案をいただきました。毎回、大変感謝しております。ご応募全員に参加報酬したいところですが、皆様の今後のご活躍を祈念しながら、ここに心より御礼を申し上げます。moonkettle

```html
<!DOCTYPE html>
<html lang="ja">
<head>
<meta charset="utf-8">
<title>おもいやりの英会話例文集</title>
<link href="https://fonts.googleapis.com/css2?family=Noto+Sans+JP:wght@400;500;700;900&family=Montserrat:wght@300;400&display=swap" rel="stylesheet">
<style>
  :root {
    --teal: #3ea9a5;
    --teal-dark: #2a8c88;
    --ink: #2b2b2b;
    --grey: #555;
    --line-icon: #e6ecec;
    --rule: #cfdede;
    --paper: #ffffff;
  }
  html, body { margin: 0; padding: 0; overflow: hidden; }
  body { width: 826px; height: 1200px; background: var(--paper); font-family: "Noto Sans JP", sans-serif; color: var(--ink); }
  .cover { position: relative; width: 826px; height: 1200px; overflow: hidden; background: var(--paper); }

  .motif { position: absolute; background: var(--line-icon); border-radius: 14px; }

  .title-block { position: absolute; top: 70px; left: 0; width: 100%; text-align: center; }
  .title-main { font-size: 78px; font-weight: 500; letter-spacing: 12px; margin: 0; line-height: 1; }
  .title-no { font-size: 52px; font-weight: 500; margin: 28px 0 30px; line-height: 1; }
  .title-sub { font-size: 70px; font-weight: 500; letter-spacing: 10px; margin: 0; line-height: 1; }
  .title-en { font-family: "Montserrat", sans-serif; color: var(--teal); font-size: 16px; letter-spacing: 3px; margin-top: 34px; }

  .credits { position: absolute; top: 436px; left: 0; width: 100%; text-align: center; color: var(--grey); }
  .supervisor { font-size: 22px; letter-spacing: 2px; }
  .supervisor small, .authors small { font-size: 14px; margin-right: 14px; }
  .authors { font-size: 15px; margin-top: 18px; letter-spacing: 1px; }

  .band { position: absolute; top: 526px; left: 0; width: 100%; height: 350px; background: var(--teal); }
  .band-word { position: absolute; top: 30px; left: 0; width: 100%; text-align: center; font-family: "Montserrat", sans-serif; font-weight: 300; font-size: 92px; letter-spacing: 18px; color: rgba(255,255,255,0.6); line-height: 1; }

  .audio { position: absolute; top: 160px; left: 36px; width: 300px; color: #fff; }
  .audio-tag { position: absolute; left: 0; top: 22px; width: 20px; height: 40px; font-size: 15px; line-height: 20px; writing-mode: vertical-rl; }
  .audio-icon { position: absolute; left: 90px; top: 0; width: 40px; height: 40px; }
  .audio-title { position: absolute; left: 30px; top: 46px; font-size: 34px; font-weight: 700; white-space: nowrap; letter-spacing: 1px; }
  .audio-note { position: absolute; left: 44px; top: 100px; font-size: 18px; line-height: 1.5; white-space: nowrap; }

  .pitch { position: absolute; top: 150px; left: 400px; width: 412px; height: 192px; background: var(--paper); padding: 14px 14px; box-sizing: border-box; }
  .pitch p { margin: 0; font-size: 17px; line-height: 1.95; color: var(--ink); border-bottom: 1px solid var(--rule); white-space: nowrap; }
  .pitch .fine { font-size: 10.5px; color: var(--teal-dark); border: 0; line-height: 1.8; }

  .closing { position: absolute; top: 910px; left: 0; width: 100%; text-align: center; }
  .closing-lead { display: inline-block; font-size: 22px; color: var(--grey); letter-spacing: 2px; padding: 0 26px; border-left: 2px solid var(--teal); border-right: 2px solid var(--teal); line-height: 1.3; }
  .closing-mid { font-size: 46px; font-weight: 700; color: var(--teal-dark); margin-top: 28px; letter-spacing: 1px; line-height: 1.2; }
  .closing-big { font-size: 92px; font-weight: 900; color: var(--teal); line-height: 1.1; margin-top: 6px; letter-spacing: 6px; }
</style>
</head>
<body>
<main class="cover">
  <div class="motif" style="left:30px;top:30px;width:70px;height:70px" role="img" aria-label="和食のお椀の線画アイコン"></div>
  <div class="motif" style="left:25px;top:300px;width:80px;height:70px" role="img" aria-label="扇子の線画アイコン"></div>
  <div class="motif" style="left:15px;top:400px;width:70px;height:120px" role="img" aria-label="電波塔の線画アイコン"></div>
  <div class="motif" style="left:720px;top:25px;width:85px;height:75px" role="img" aria-label="富士山の線画アイコン"></div>
  <div class="motif" style="left:740px;top:160px;width:60px;height:70px" role="img" aria-label="地図の線画アイコン"></div>
  <div class="motif" style="left:720px;top:320px;width:85px;height:100px" role="img" aria-label="城の線画アイコン"></div>
  <div class="motif" style="left:730px;top:455px;width:70px;height:55px" role="img" aria-label="スーツケースの線画アイコン"></div>

  <header class="title-block">
    <h1 class="title-main">おもいやり</h1>
    <div class="title-no">の</div>
    <div class="title-sub">英会話例文集</div>
    <div class="title-en">English Phrases for Warm Welcomes</div>
  </header>

  <section class="credits">
    <div class="supervisor"><small>監修</small>森川啓一</div>
    <div class="authors"><small>著者</small>森川啓一・北野麻衣子・浅井里奈・高瀬加奈子</div>
  </section>

  <section class="band">
    <div class="band-word">OMOIYARI</div>
    <div class="audio">
      <div class="audio-tag">別売</div>
      <svg class="audio-icon" viewBox="0 0 40 40"><path d="M6 15h7l9-8v26l-9-8H6z" fill="#fff"/><path d="M27 13c3 4 3 10 0 14M31 9c5 6 5 16 0 22" stroke="#fff" stroke-width="2.5" fill="none" stroke-linecap="round"/></svg>
      <div class="audio-title">音声データ</div>
      <div class="audio-note">CD6枚相当分<br>本書完全対応</div>
    </div>
    <div class="pitch">
      <p>来日観光客3,000万人時代へ突入!</p>
      <p>東京五輪でさらに増える海外からのお客様を</p>
      <p>おもてなしするために必携の書。</p>
      <p class="fine">別売りの音声データを合わせて使えば完全学習が可能です。</p>
    </div>
  </section>

  <section class="closing">
    <div class="closing-lead">お客様を迎える多様な場面で役立つ</div>
    <div class="closing-mid">5,000以上の会話表現を収録した</div>
    <div class="closing-big">総合表現集</div>
  </section>
</main>
</body>
</html>
```